Marrowind Leaf range - labels for a range of teas.

Our company name is Marrowind Leaf Company - based in Melbourne, Australia. We have a current logo project with Pixel Harbor.

We offer a range of top quality teas - black, green, white, oolongs, herbals, flavoured teas. From Japan, Assam, Darjeeling, Ceylon, Africa and elsewhere. The very best loose teas, and some pyramid tea bags too.

We cover some blends : English Breakfast, African Breakfast, Ceylon Breakfast, Earl Grey amongst them.

And herbal variants: lemon grass and ginger, chamomile, peppermint, rooibos and chilli.

And fruit teas.... and flavoured teas like vanilla, peach and raspberry.

We aim to occupy a modern, contemporary, sophisticated and global space.... but we can be funky too, especially with the fruit and herbal offers. Quality is paramount ! We do not aim to have the biggest range of teas, but we are very particular. And we source directly from origin.... fresh quality teas.

Would lean towards black teas being on a black background label, green teas on a green background, white etas on a white background, herbals maybe on a straw or suitable background, and flavoured teas on a specific background colour too....maybe fuschia? Violet ? But colourful is key.

The panel should indicate teas being Loose or Pyramid bags. And the nett weight should be shown.... Loose could be for example 75 gr, 125 gr 250 gr etc.. And pyramids would show the number of pyramids and weight, example 20 x Pyramids 50 gr
50 Pyramids 150 gr etc.

And 'Marrowind Leaves' or 'Marrowind Leaf Company' should be on the panel too. Melbourne can appear as well if it gels with the total look.

There will need to be 2 lines - in order or juxtaposed, doesn't matter - showing the origin and 'mark' and grade. Example being:
Ceylon
Kenwick Pekoe

or

Darjeeling
Melgara TGFOP1

or

China
Jasmine Leaf

We just need templates to cover the different types of tea - black, green, white, herbal, flavoured - as there are too many (and changing) types of tea in the range .

Any questions...please ask...

Thanks

Reason: Needs to have alater deadline than the current Logo Project associated with the same Marrowind Leaf Company start up.

Target Market(s)

Sophisticated. Real tea lovers. Discriminating tastes.

Industry/Entity Type

Weight

Font styles to use
Sans Serif

Requirements
Must have
• Sophisticated
Cool
Premium quality branding
Bold
Uber modern
Nice to have
• BOLD text.....
Cool fonts....
Pretty bold and minimalist - ultra modern if possible....uber modern
Bright colours and use of black and white..... Not really into pastels etc..

Lots of black colour too is a likely plus
Should not have
• Frilly stuff

```html
<!DOCTYPE html>
<html lang="en">
<head>
<meta charset="utf-8">
<title>Marrowind Leaf Co — Tea Range Labels</title>
<link rel="stylesheet" href="https://fonts.googleapis.com/css2?family=Oswald:wght@500&family=Nunito:wght@800&family=Roboto:wght@400;700&display=swap">
<style>
  :root {
    --bg: #ffffff;
    --pouch: #0b0b0b;
    --pouch-edge: #1c1c1c;
    --white: #f4f4f4;
    --muted: #d6d6d6;
    --hang: #3a3a3a;
    --rule: #6cc04a;
    --green: #6cc04a;
    --oolong: #b64fae;
    --black-tea: #6d6d6d;
    --leaf-light: #b7e04a;
    --leaf-dark: #6aa82e;
  }
  * { margin: 0; padding: 0; box-sizing: border-box; }
  html, body {
    width: 1200px; height: 714px; overflow: hidden;
    background: var(--bg);
  }
  .range { position: relative; width: 1200px; height: 714px; }

  .pouch {
    position: absolute; top: 100px; width: 303px; height: 510px;
    background: var(--pouch);
    border: 1px solid var(--pouch-edge);
    border-radius: 6px;
    color: var(--white);
    overflow: hidden;
  }
  .pouch--green  { left: 70px;  --accent: var(--green); }
  .pouch--oolong { left: 448px; --accent: var(--oolong); }
  .pouch--black  { left: 826px; --accent: var(--black-tea); }

  .pouch__hang {
    position: absolute; top: 14px; left: 133px; width: 36px; height: 9px;
    border-radius: 5px; background: var(--hang);
  }
  .brand-block {
    position: absolute; top: 150px; left: 50px; width: 203px; height: 64px;
    border-top: 2px solid var(--rule);
    border-bottom: 2px solid var(--rule);
    display: flex; align-items: center; justify-content: center;
  }
  .brand {
    font-family: "Oswald", sans-serif; font-weight: 500;
    font-size: 22px; letter-spacing: 1.6px; line-height: 1;
    white-space: nowrap; color: var(--white);
  }
  .brand__city {
    position: absolute; top: 221px; left: 0; width: 100%;
    text-align: center;
    font-family: "Roboto", sans-serif; font-weight: 700;
    font-size: 9px; letter-spacing: 2.5px;
    color: var(--white);
  }
  .tea-type {
    position: absolute; top: 232px; left: 0; width: 100%;
    text-align: center; white-space: nowrap;
    font-family: "Nunito", sans-serif; font-weight: 800;
    font-size: 50px; letter-spacing: -1.5px; line-height: 1;
    color: var(--accent);
  }
  .origin {
    position: absolute; top: 321px; left: 24px;
    padding-left: 8px;
    border-left: 2px solid var(--accent);
    font-family: "Roboto", sans-serif; font-weight: 700;
    font-size: 18px; line-height: 1.2;
    color: var(--white);
  }
  .leaf-art {
    position: absolute; top: 318px; left: 196px; width: 84px; height: 132px;
    border-radius: 8px;
    background: linear-gradient(170deg, var(--leaf-light), var(--leaf-dark));
  }
  .pack-count {
    position: absolute; top: 398px; left: 24px;
    display: flex; align-items: center; gap: 4px;
    height: 27px; padding: 0 7px;
    border: 1.5px solid var(--white); border-radius: 6px;
    font-family: "Roboto", sans-serif; color: var(--white);
  }
  .pack-count__number { font-weight: 700; font-size: 20px; line-height: 1; }
  .pack-count__label { font-size: 8px; line-height: 1.05; }
  .net-weight {
    position: absolute; bottom: 24px; right: 10px;
    font-family: "Roboto", sans-serif; font-weight: 400;
    font-size: 10px; letter-spacing: 0.2px;
    color: var(--muted);
  }
</style>
</head>
<body>
<main class="range">

  <article class="pouch pouch--green">
    <span class="pouch__hang"></span>
    <div class="brand-block"><p class="brand">MARROWIND LEAF CO</p></div>
    <p class="brand__city">MELBOURNE</p>
    <h2 class="tea-type">green tea</h2>
    <p class="origin">ceylon<br>kenwick pekoe</p>
    <div class="leaf-art" role="img" aria-label="Illustration of three green tea leaves"></div>
    <p class="pack-count"><span class="pack-count__number">20</span><span class="pack-count__label">Pyramid<br>tea bags</span></p>
    <p class="net-weight">NET WT 125 gr</p>
  </article>

  <article class="pouch pouch--oolong">
    <span class="pouch__hang"></span>
    <div class="brand-block"><p class="brand">MARROWIND LEAF CO</p></div>
    <p class="brand__city">MELBOURNE</p>
    <h2 class="tea-type">oolong tea</h2>
    <p class="origin">china<br>jasmine leaf</p>
    <div class="leaf-art" role="img" aria-label="Illustration of three green tea leaves"></div>
    <p class="pack-count"><span class="pack-count__number">20</span><span class="pack-count__label">Pyramid<br>tea bags</span></p>
    <p class="net-weight">NET WT 125 gr</p>
  </article>

  <article class="pouch pouch--black">
    <span class="pouch__hang"></span>
    <div class="brand-block"><p class="brand">MARROWIND LEAF CO</p></div>
    <p class="brand__city">MELBOURNE</p>
    <h2 class="tea-type">black tea</h2>
    <p class="origin">china<br>jasmine leaf</p>
    <div class="leaf-art" role="img" aria-label="Illustration of three green tea leaves"></div>
    <p class="pack-count"><span class="pack-count__number">20</span><span class="pack-count__label">Pyramid<br>tea bags</span></p>
    <p class="net-weight">NET WT 125 gr</p>
  </article>

</main>
</body>
</html>
```